Harborline Security and Surveillance Business Card

Business Card Design - Company Name:Freedom Security and SurveillanceWe are a Security Systems Integrator Specializing in Security Systems/ Video Surveillance and Access Control. Our areas of expertise are:Security SystemsVideo SurveillanceAccess ControlFire Alarm SystemsNetwork CablingCellular BoostersMy input is the Front of the Card is: logo, name of Business, My Name, Phone Number, and email.Rear of Card is the 6 areas of expertise, I just dont want the front to be very busy.
Name: Tom Werner
Title: President
Email: tom@harborlinesecsys.example
website: harborlinesecsys.example

```html
<!DOCTYPE html>
<html lang="en">
<head>
<meta charset="utf-8">
<title>Harborline Security and Surveillance Business Card</title>
<link rel="stylesheet" href="https://fonts.googleapis.com/css2?family=Source+Sans+3:wght@300;400;600&display=swap">
<style>
  :root {
    --page-bg: #f2f3f5;
    --brand-blue: #045bbb;
    --curve-grey: #b4b7bc;
    --card-white: #ffffff;
    --back-dark: #1b1d20;
    --service-text: #d3d6da;
    --text-white: #ffffff;
  }
  * { margin: 0; padding: 0; box-sizing: border-box; }
  html, body {
    width: 1133px; height: 1200px; overflow: hidden;
    background: var(--page-bg);
    font-family: "Source Sans 3", sans-serif;
  }
  .card {
    position: absolute; left: 218px;
    width: 696px; height: 398px; overflow: hidden;
  }
  .card-front { top: 152px; background: var(--card-white); }
  .card-back { top: 648px; background: var(--back-dark); }

  .front-panel { position: absolute; inset: 0; }

  .company-name {
    position: absolute; left: 330px; top: 140px; width: 320px;
    text-align: center; color: var(--brand-blue); font-weight: 600;
    text-transform: uppercase; letter-spacing: 2px; line-height: 1.1;
  }
  .company-name .line-main { display: block; font-size: 27px; }
  .company-name .line-sub { display: block; font-size: 13px; letter-spacing: 4px; margin-top: 4px; }
  .brand-dot {
    position: absolute; left: 474px; top: 100px;
    width: 30px; height: 30px; border-radius: 50%; background: var(--brand-blue);
  }

  .contact-block { position: absolute; left: 36px; top: 262px; color: var(--text-white); }
  .person-name { font-size: 27px; font-weight: 600; line-height: 1; text-transform: uppercase; }
  .person-title { font-size: 19px; font-weight: 400; margin-top: 4px; }
  .contact-list { list-style: none; margin-top: 12px; }
  .contact-list li { display: flex; align-items: center; gap: 9px; font-size: 19px; line-height: 23px; }
  .contact-list svg { width: 16px; height: 16px; flex: none; }

  .back-name {
    position: absolute; left: 0; right: 0; top: 160px;
    text-align: center; color: var(--brand-blue); font-weight: 600;
    font-size: 34px; letter-spacing: 3px; text-transform: uppercase;
  }
  .services {
    position: absolute; left: 0; right: 0; top: 326px;
    text-align: center; color: var(--service-text);
    font-size: 19px; font-weight: 300; line-height: 24px;
  }
  .services .sep {
    display: inline-block; width: 6px; height: 6px; border-radius: 50%;
    background: var(--brand-blue); margin: 0 3px 2px 6px; vertical-align: middle;
  }
</style>
</head>
<body>
  <section class="card card-front">
    <svg class="front-panel" viewBox="0 0 696 398" width="696" height="398" aria-hidden="true">
      <path d="M282 0 C272 120 304 250 468 398" fill="none" stroke="var(--curve-grey)" stroke-width="4"/>
      <path d="M0 0 H278 C268 120 300 250 462 398 H0 Z" fill="var(--brand-blue)"/>
    </svg>

    <span class="brand-dot"></span>
    <h1 class="company-name">
      <span class="line-main">Harborline Security</span>
      <span class="line-sub">and Surveillance</span>
    </h1>

    <div class="contact-block">
      <h2 class="person-name">Tom Werner</h2>
      <p class="person-title">President</p>
      <ul class="contact-list">
        <li>
          <svg viewBox="0 0 16 16" aria-hidden="true"><rect x="1" y="3" width="14" height="10" rx="1" fill="#fff"/><path d="M1.5 4 L8 9 L14.5 4" fill="none" stroke="var(--brand-blue)" stroke-width="1.4"/></svg>
          tom@harborlinesecsys.example
        </li>
        <li>
          <svg viewBox="0 0 16 16" aria-hidden="true"><circle cx="8" cy="8" r="7.5" fill="#fff"/><path d="M4 4 Q7 5 6 8 Q5 10 7 12 M10 3 Q9 6 12 7" fill="none" stroke="var(--brand-blue)" stroke-width="1.4"/></svg>
          harborlinesecsys.example
        </li>
      </ul>
    </div>
  </section>

  <section class="card card-back">
    <p class="back-name">Harborline</p>
    <p class="services">
      Security Systems<span class="sep"></span>Video Surveillance<span class="sep"></span>Access Control<br>
      Fire Alarm Systems<span class="sep"></span>Network Cabling<span class="sep"></span>Cellular Boosters
    </p>
  </section>
</body>
</html>
```